Business Card Design and stationary (thank you cards)

I am basically starting a "handyman" business but have a little ego issue with that term. I have been a professional in the design and construction business for 30 years. I want simple…I will define the scope of work I do as i move forward, and it can vary and i want it to vary.

Target Market(s)

Homeowners mostly

Industry/Entity Type

Business

Contact Information for Business Card

Company Name is "Fix 9 the Nest" Dale R. Hobbins, 42 Bellamy Orchard Lane, Stonington, Ct, 06412 (but I may want to use a PO Box), Phone is 860-555-0172, email is dhobbins418@quillpost.example,

Font styles to use
Sans Serif

Requirements
Should not have
• anything pre designed….hammers or whatever…custom lines to make home features as shone but simple and elegant

```html
<!DOCTYPE html>
<html lang="en">
<head>
<meta charset="utf-8">
<title>Fix 9 the Nest — Business Card</title>
<link rel="stylesheet" href="https://fonts.googleapis.com/css2?family=Inter:wght@600;700&display=swap">
<style>
  :root {
    --card-bg: #ffffff;
    --ink: #000000;
  }
  html, body {
    margin: 0;
    padding: 0;
    width: 1200px;
    height: 702px;
    overflow: hidden;
    background: var(--card-bg);
  }
  .card {
    position: relative;
    width: 1200px;
    height: 702px;
    background: var(--card-bg);
    color: var(--ink);
    font-family: "Inter", "Helvetica Neue", Arial, sans-serif;
  }
  .card__line {
    position: absolute;
    right: 53px;
    margin: 0;
    line-height: 1;
    white-space: nowrap;
    text-align: right;
  }
  .company-name {
    top: 136px;
    font-size: 68px;
    font-weight: 700;
    letter-spacing: -0.5px;
  }
  .owner-name {
    top: 240px;
    font-size: 48px;
    font-weight: 700;
    letter-spacing: -0.3px;
  }
  .contact {
    font-size: 26px;
    font-weight: 600;
  }
  .contact--address { top: 347px; }
  .contact--phone { top: 434px; }
  .contact--email { top: 523px; }
</style>
</head>
<body>
  <main class="card">
    <h1 class="card__line company-name">Fix 9 the Nest</h1>
    <h2 class="card__line owner-name">Dale R. Hobbins</h2>
    <p class="card__line contact contact--address">42 Bellamy Orchard Lane, Fernhollow</p>
    <p class="card__line contact contact--phone">860-555-0172</p>
    <p class="card__line contact contact--email">dhobbins418@quillpost.example</p>
  </main>
</body>
</html>
```